Fund Harbor

We need desigin for our main page(concept will be used for other pages also).
We already have a logo, and moqup of our main page(see attch).
You could change layers and positions on moqup, but please use logo, and its colors in design creating. (We have logo in different colors, i attached 2 samples, so you could use also another colors if you wish).

Our bussinees will be something similar to LaunchPeak or Backwise.co, but with some special features. So main idea: start-ups, donations, investemnets

Designs were prefer:
http://backwise.co/
http://www.launchpeak.com/

Target Market(s)

Clients are middle aged persons, who interested in new start-ups, investments and so on.

Requirements
Must have
• Design must be neat

```html
<!DOCTYPE html>
<html lang="en">
<head>
<meta charset="utf-8">
<title>Fund Harbor</title>
<link href="https://fonts.googleapis.com/css2?family=Arimo:wght@400;700&display=swap" rel="stylesheet">
<style>
:root{
  --navy:#1c3a66;
  --navy-dark:#15305a;
  --footer:#1d3b69;
  --footer-line:#2c4d80;
  --blue-text:#1f4f8a;
  --grey-top:#cdcdcd;
  --grey-low:#e4e4e4;
  --panel:#f3f3f3;
  --border:#c9c9c9;
  --text:#666;
  --muted:#8a8a8a;
  --orange:#f79a12;
  --link-blue:#4d8ad6;
}
*{box-sizing:border-box;margin:0;padding:0}
html,body{width:1111px;height:1200px;overflow:hidden}
body{font-family:"Arimo",Arial,sans-serif;background:#fff;position:relative;color:var(--text)}
.abs{position:absolute}
.hero-bg{left:0;top:0;width:1111px;height:316px;background:var(--grey-top)}
.hero-bg-low{left:0;top:316px;width:1111px;height:73px;background:var(--grey-low)}

/* header */
.brand{left:145px;top:14px;display:flex;align-items:center;gap:8px}
.brand-mark{width:30px;height:30px;border-radius:50%;background:var(--navy)}
.brand-name{font-size:22px;font-weight:700;color:var(--navy);letter-spacing:-.3px}
.nav{left:377px;top:30px;display:flex;align-items:center}
.nav a{font-size:12px;color:var(--blue-text);text-decoration:none;margin-right:54px}
.nav a.active{background:var(--navy);color:#fff;border-radius:3px;padding:11px 18px;box-shadow:0 1px 2px rgba(0,0,0,.4);margin-right:36px}
.search{left:787px;top:10px;width:178px;height:25px;background:#f6f6f6;border:1px solid #bcbcbc;border-radius:3px;font-size:9px;color:#999;padding:7px 0 0 23px}
.search svg{position:absolute;left:7px;top:6px}
.search .clear{position:absolute;right:4px;top:5px;width:14px;height:14px;border-radius:50%;background:#333}
.lang{left:787px;top:41px;width:178px;height:24px;background:#f6f6f6;border:1px solid #bcbcbc;border-radius:3px;font-size:10px;font-style:italic;color:#888;padding:6px 0 0 7px}
.lang svg{position:absolute;right:6px;top:8px}

/* top panels */
.panel{top:108px;height:253px;background:var(--panel);border:1px solid var(--border);border-radius:3px}
.stats{left:144px;width:207px;padding:6px 12px}
.stats li{list-style:none;font-size:10px;color:#777;height:31.6px;display:flex;align-items:center;gap:10px;border-bottom:1px solid #ddd}
.stats li:last-child{border-bottom:none}
.video{left:360px;width:367px;border:none;overflow:hidden;border-radius:2px;box-shadow:0 3px 6px rgba(0,0,0,.25)}
.video-screen{height:230px;background:radial-gradient(circle at 50% 55%,#2a6ec0,#1f4a8a 60%,#1a3a6e);display:flex;flex-direction:column;align-items:center;justify-content:center;gap:12px}
.video-title{color:#fff;font-weight:700;font-size:15px;letter-spacing:1.5px}
.video-bar{height:23px;background:#f0f0f0;border-top:2px solid #d22;font-size:7px;color:#888;display:flex;align-items:center;padding:0 8px;gap:10px}
.login{left:736px;width:229px;padding:20px 12px}
.tabs{display:flex;justify-content:space-between}
.tab{width:91px;height:29px;font-size:11px;display:flex;align-items:center;justify-content:center;border-radius:2px}
.tab.on{background:var(--navy);color:#fff}
.tab.off{background:#d2d2d2;color:#fff}
.login label{display:block;font-size:9px;color:#888;letter-spacing:.5px;margin:9px 0 3px}
.field{height:25px;background:#fff;border:1px solid #aaa;border-radius:2px}
.forgot{font-size:8px;color:var(--blue-text);text-decoration:underline;margin-top:11px;display:block}
.remember{font-size:8px;color:#666;display:flex;align-items:center;gap:5px;margin-top:8px}
.box{width:10px;height:10px;border:1px solid #888;background:#fff;display:flex;align-items:center;justify-content:center}
.login-btn{margin:16px auto 0;width:92px;height:30px;background:var(--orange);color:#fff;font-weight:700;font-size:11px;display:flex;align-items:center;justify-content:center;border-radius:2px;letter-spacing:.5px}

/* projects */
.col-title{top:423px;width:180px;text-align:center;font-size:14px;color:var(--blue-text)}
.card{top:452px;width:180px;height:328px;background:#f7f7f7;border:1px solid #ddd;padding:3px}
.card-in{background:#fff;height:100%;border:1px solid #e2e2e2;position:relative}
.card h3{font-weight:400;font-size:14px;color:#555;text-align:center;height:36px;line-height:36px}
.card .photo{height:90px;background:linear-gradient(160deg,#5f7f9a,#c9c9c6 45%,#6d6154)}
.card p{font-size:9px;line-height:14.5px;color:#8a8a8a;padding:11px 8px 0;letter-spacing:.2px}
.card ul{list-style:none;padding:6px 8px 0}
.card li{font-size:9px;color:#555;text-decoration:underline;height:21px;line-height:21px;letter-spacing:.3px}
.card .foot{position:absolute;left:0;right:0;bottom:0;height:42px;background:#f2f2f2;padding:7px 7px}
.invest{width:88px;height:26px;background:var(--navy-dark);color:#fff;font-size:11px;display:flex;align-items:center;justify-content:center;border-radius:2px;box-shadow:0 1px 2px rgba(0,0,0,.4)}

/* footer */
.footer{left:0;top:832px;width:1111px;height:368px;background:var(--footer);border-top:7px solid #0f2442}
.fcol{top:858px}
.fcol h4{font-weight:400;color:#fff;font-size:14.5px;margin-bottom:20px;display:flex;align-items:center;gap:8px}
.fcol p{font-size:9.5px;line-height:14.5px;color:#9eb0c8;letter-spacing:.5px;margin-bottom:11px}
.fcol p span{color:var(--link-blue)}
.vline{top:858px;width:0;height:250px;border-left:1px dashed #3a5d91}
.readmore{font-size:9.5px;color:var(--orange);text-decoration:underline;letter-spacing:.5px}
.contact-name{color:#fff;font-weight:700;font-size:9.5px;display:flex;gap:8px;align-items:center}
.socials{display:flex;gap:5px}
.socials div{width:22px;height:22px;border-radius:3px}
.fbottom{left:145px;top:1144px;width:820px;border-top:1px solid #0f2442;padding-top:22px;display:flex;justify-content:space-between;font-size:9.5px;color:#fff;letter-spacing:.4px}
</style>
</head>
<body>
<div class="abs hero-bg"></div>
<div class="abs hero-bg-low"></div>

<header>
  <div class="abs brand"><div class="brand-mark"></div><span class="brand-name">Fund Harbor</span></div>
  <nav class="abs nav">
    <a class="active" href="#">How it Work</a>
    <a href="#">Projects Review</a>
    <a href="#">Virtual Office</a>
  </nav>
  <div class="abs search">
    <svg width="11" height="11" viewBox="0 0 11 11"><circle cx="4.5" cy="4.5" r="3.3" fill="none" stroke="#888" stroke-width="1.3"/><line x1="7" y1="7" x2="10" y2="10" stroke="#888" stroke-width="1.5"/></svg>
    Search...
    <div class="clear"></div>
  </div>
  <div class="abs lang">English
    <svg width="12" height="7" viewBox="0 0 12 7"><polyline points="1,1 6,6 11,1" fill="none" stroke="#bbb" stroke-width="1.4"/></svg>
  </div>
</header>

<section>
  <ul class="abs panel stats">
    <li><svg width="11" height="9" viewBox="0 0 11 9"><rect x=".5" y="1.5" width="7" height="7" fill="none" stroke="#999"/><polyline points="2,4 4,6.5 10,.5" fill="none" stroke="#777" stroke-width="1.3"/></svg>$50,000,000 of investments</li>
    <li><svg width="11" height="9" viewBox="0 0 11 9"><rect x=".5" y="1.5" width="7" height="7" fill="none" stroke="#999"/><polyline points="2,4 4,6.5 10,.5" fill="none" stroke="#777" stroke-width="1.3"/></svg>1600 Start-Ups</li>
    <li><svg width="11" height="9" viewBox="0 0 11 9"><rect x=".5" y="1.5" width="7" height="7" fill="none" stroke="#999"/><polyline points="2,4 4,6.5 10,.5" fill="none" stroke="#777" stroke-width="1.3"/></svg>700 Organizations</li>
    <li><svg width="11" height="9" viewBox="0 0 11 9"><rect x=".5" y="1.5" width="7" height="7" fill="none" stroke="#999"/><polyline points="2,4 4,6.5 10,.5" fill="none" stroke="#777" stroke-width="1.3"/></svg>10,000 Investors</li>
    <li><svg width="11" height="9" viewBox="0 0 11 9"><rect x=".5" y="1.5" width="7" height="7" fill="none" stroke="#999"/><polyline points="2,4 4,6.5 10,.5" fill="none" stroke="#777" stroke-width="1.3"/></svg>5000 Employees</li>
    <li><svg width="11" height="9" viewBox="0 0 11 9"><rect x=".5" y="1.5" width="7" height="7" fill="none" stroke="#999"/><polyline points="2,4 4,6.5 10,.5" fill="none" stroke="#777" stroke-width="1.3"/></svg>2000 Partners</li>
    <li><svg width="11" height="9" viewBox="0 0 11 9"><rect x=".5" y="1.5" width="7" height="7" fill="none" stroke="#999"/><polyline points="2,4 4,6.5 10,.5" fill="none" stroke="#777" stroke-width="1.3"/></svg>$ 10,000,000 of Profit</li>
  </ul>

  <div class="abs panel video">
    <div class="video-screen">
      <svg width="50" height="50" viewBox="0 0 50 50"><circle cx="25" cy="25" r="22" fill="none" stroke="#10223f" stroke-width="3"/><polygon points="20,15 34,25 20,35" fill="#10223f"/></svg>
      <div class="video-title">FUND HARBOR</div>
    </div>
    <div class="video-bar">
      <svg width="8" height="9" viewBox="0 0 8 9"><rect x="0" y="0" width="2.5" height="9" fill="#999"/><rect x="5" y="0" width="2.5" height="9" fill="#999"/></svg>
      <svg width="11" height="9" viewBox="0 0 11 9"><polygon points="0,3 3,3 6,0 6,9 3,6 0,6" fill="#999"/></svg>
      <span>1:50 / 1:50</span>
      <span style="margin-left:auto">240p</span>
      <svg width="10" height="9" viewBox="0 0 10 9"><rect x=".5" y=".5" width="9" height="8" fill="none" stroke="#999"/></svg>
      <svg width="10" height="9" viewBox="0 0 10 9"><rect x=".5" y=".5" width="9" height="8" fill="none" stroke="#999" stroke-dasharray="2 2"/></svg>
    </div>
  </div>

  <form class="abs panel login">
    <div class="tabs"><div class="tab on">Log In</div><div class="tab off">Register</div></div>
    <label>E-mail or Phone</label>
    <div class="field"></div>
    <label>Password</label>
    <div class="field"></div>
    <a class="forgot">I forgot my password</a>
    <div class="remember"><div class="box"><svg width="8" height="7" viewBox="0 0 8 7"><polyline points="1,3.5 3,6 7,1" fill="none" stroke="#2a7a3a" stroke-width="1.5"/></svg></div>Remember me</div>
    <div class="login-btn">LOG IN</div>
  </form>
</section>

<section>
  <h2 class="abs col-title" style="left:145px">Recommended</h2>
  <h2 class="abs col-title" style="left:358px">Popular</h2>
  <h2 class="abs col-title" style="left:569px">Most Invested</h2>
  <h2 class="abs col-title" style="left:784px">New</h2>

  <article class="abs card" style="left:145px"><div class="card-in">
    <h3>Project - A</h3>
    <div class="photo" role="img" aria-label="Laptop on a desk"></div>
    <p>Sed sit amet nulla et dui faucibus bibendum. Suspendisse id nulla ac felis commodo blandit.</p>
    <ul><li>$90,000 invested</li><li>70% success</li><li>200 investors</li><li>23 days left</li></ul>
    <div class="foot"><div class="invest">INVEST</div></div>
  </div></article>
  <article class="abs card" style="left:358px"><div class="card-in">
    <h3>Project - B</h3>
    <div class="photo" role="img" aria-label="Laptop on a desk"></div>
    <p>Sed sit amet nulla et dui faucibus bibendum. Suspendisse id nulla ac felis commodo blandit.</p>
    <ul><li>$90,000 invested</li><li>70% success</li><li>200 investors</li><li>23 days left</li></ul>
    <div class="foot"><div class="invest">INVEST</div></div>
  </div></article>
  <article class="abs card" style="left:569px"><div class="card-in">
    <h3>Project - C</h3>
    <div class="photo" role="img" aria-label="Laptop on a desk"></div>
    <p>Sed sit amet nulla et dui faucibus bibendum. Suspendisse id nulla ac felis commodo blandit.</p>
    <ul><li>$90,000 invested</li><li>70% success</li><li>200 investors</li><li>23 days left</li></ul>
    <div class="foot"><div class="invest">INVEST</div></div>
  </div></article>
  <article class="abs card" style="left:784px"><div class="card-in">
    <h3>Project - D</h3>
    <div class="photo" role="img" aria-label="Laptop on a desk"></div>
    <p>Sed sit amet nulla et dui faucibus bibendum. Suspendisse id nulla ac felis commodo blandit.</p>
    <ul><li>$90,000 invested</li><li>70% success</li><li>200 investors</li><li>23 days left</li></ul>
    <div class="foot"><div class="invest">INVEST</div></div>
  </div></article>
</section>

<footer>
  <div class="abs footer"></div>
  <div class="abs vline" style="left:395px"></div>
  <div class="abs vline" style="left:713px"></div>

  <div class="abs fcol" style="left:145px;width:200px">
    <h4>Fund Harbor informations</h4>
    <p>Donec eget est mi, non vehicula sem. Sed pretium, metus ut imperdiet lacinia, neque ipsum vestibulum eros, eu porttitor arcu dui et metus.</p>
    <p>Donec eget est mi, non vehicula sem. Sed pretium, metus ut imperdiet lacinia, neque ipsum vestibulum eros, eu porttitor arcu dui et metus.</p>
    <p>Donec eget est mi, non vehicula sem. Sed pretium, metus ut imperdiet lacinia, neque ipsum vestibulum eros, eu porttitor arcu dui et metus.</p>
    <a class="readmore">Read More&gt;</a>
  </div>

  <div class="abs fcol" style="left:454px;width:210px">
    <h4><span style="width:15px;height:15px;background:#6ab4e8;border-radius:2px;display:inline-block"></span>Latest tweet</h4>
    <p>Suspendisse <span>vulputate sagittis leo eu</span> tempus. Vivamus imperdiet, ligula ultricies facilisis <span>sed mattis</span> odio dolor a diam. Nulla facilisi.</p>
    <p style="margin-top:22px">Suspendisse <span>vulputate sagittis leo eu</span> tempus. Vivamus imperdiet, ligula ultricies facilisis <span>sed mattis</span> odio dolor a diam. Nulla facilisi.</p>
    <p style="margin-top:22px">Suspendisse <span>vulputate sagittis leo eu</span> tempus. Vivamus imperdiet, ligula ultricies facilisis <span>sed mattis</span> odio dolor a diam. Nulla facilisi.</p>
  </div>

  <div class="abs fcol" style="left:784px;width:190px">
    <h4>Contact Us</h4>
    <div class="contact-name"><svg width="11" height="10" viewBox="0 0 11 10"><polygon points="5.5,0 11,5 9,5 9,10 2,10 2,5 0,5" fill="#aab"/></svg>Fund Harbor</div>
    <p style="margin-top:9px">88 Harbor Lane, Suite 12,<br>Port Alden 40210</p>
    <p style="display:flex;gap:8px;align-items:center"><svg width="11" height="8" viewBox="0 0 11 8"><rect x="0" y="2" width="11" height="6" rx="1" fill="#aab"/><rect x="2" y="0" width="7" height="3" rx="1" fill="#aab"/></svg>+00-555-0147-220</p>
    <p style="display:flex;gap:8px;align-items:center;color:var(--link-blue)"><svg width="11" height="8" viewBox="0 0 11 8"><rect x="0" y="0" width="11" height="8" fill="#aab"/><polyline points="0,0 5.5,4.5 11,0" fill="none" stroke="#1d3b69"/></svg>hello@fundharbor-studio.com</p>
    <h4 style="margin-top:40px;margin-bottom:12px">Follow Us On</h4>
    <div class="socials">
      <div style="background:#5fb0e4"></div>
      <div style="background:#3b5a98"></div>
      <div style="background:#c4302b"></div>
      <div style="background:#4a7cc0"></div>
      <div style="background:#f08a24"></div>
    </div>
  </div>

  <div class="abs fbottom"><span>© 2013 fund harbor</span><span>Privacy Policy</span></div>
</footer>
</body>
</html>
```